Business card for a new cabinet shop company named Marlowe Cabinets for high end cabinets

Design a business card, thinking dark rich green with colours to speak of high end luxury ie; cream, gold, black possibly

Peter Lindqvar
Director Craftsman
Email: info@marlowecabinets.com.au
Instagram : @marlowe.cabinets

```html
<!DOCTYPE html>
<html lang="en">
<head>
<meta charset="utf-8">
<title>Marlowe Cabinets – Business Card</title>
<link rel="stylesheet" href="https://fonts.googleapis.com/css2?family=Montserrat:wght@400;700&family=Open+Sans:wght@400&display=swap">
<style>
  :root {
    --page: #e9e9e6;
    --green: #07412a;
    --gold: #d7b25c;
    --gold-light: #f3dc93;
    --gold-dark: #a97f2c;
    --ink: #1b1a17;
    --cream: #f4efe2;
    --black: #0b0b0b;
  }
  * { box-sizing: border-box; margin: 0; padding: 0; }
  html, body {
    width: 1138px; height: 1200px; overflow: hidden;
    background: var(--page);
  }
  .sheet {
    position: relative; width: 1138px; height: 1200px;
    display: flex; flex-direction: column; align-items: center; justify-content: center; gap: 46px;
  }
  .card {
    position: relative; width: 940px; height: 537px;
    background: var(--green); overflow: hidden;
    box-shadow: 0 6px 22px rgba(0,0,0,.18);
  }
  /* Front */
  .card-front { display: flex; align-items: center; justify-content: center; }
  .brand-front {
    font-family: "Montserrat", sans-serif; font-weight: 400; color: var(--gold);
    text-align: center; line-height: 1;
  }
  .brand-front .brand-name { display: block; font-size: 104px; letter-spacing: 1px; }
  .brand-front .brand-sub { display: block; font-size: 44px; letter-spacing: 16px; margin-top: 16px; padding-left: 16px; }

  /* Back */
  .bands { position: absolute; inset: 0; width: 100%; height: 100%; }
  .holder-name {
    position: absolute; top: 0; right: 70px; height: 86px; line-height: 90px;
    font-family: "Montserrat", sans-serif; font-weight: 700; font-size: 40px;
    color: var(--ink); letter-spacing: .5px;
  }
  .holder-title {
    position: absolute; left: 30px; top: 457px; height: 80px; line-height: 82px;
    font-family: "Montserrat", sans-serif; font-weight: 700; font-size: 34px;
    color: var(--ink);
  }
  .brand-back {
    position: absolute; left: 44px; top: 250px;
    font-family: "Montserrat", sans-serif; font-weight: 400; color: var(--gold); line-height: 1;
  }
  .brand-back .brand-name { display: block; font-size: 40px; }
  .brand-back .brand-sub { display: block; font-size: 15px; letter-spacing: 6px; margin-top: 6px; }
  .contact-list { position: absolute; left: 377px; top: 198px; list-style: none; }
  .contact-item {
    display: flex; align-items: center; height: 50px; margin-bottom: 41px;
    font-family: "Open Sans", sans-serif; font-size: 31px; color: var(--cream);
  }
  .contact-icon {
    width: 50px; height: 46px; margin-right: 36px; flex: none;
    background: linear-gradient(135deg, var(--gold-light), var(--gold) 55%, var(--gold-dark));
    display: flex; align-items: center; justify-content: center;
  }
</style>
</head>
<body>
<main class="sheet">
  <section class="card card-front" aria-label="Card front">
    <div class="brand-front">
      <span class="brand-name">Marlowe</span>
      <span class="brand-sub">CABINETS</span>
    </div>
  </section>

  <section class="card card-back" aria-label="Card back">
    <svg class="bands" viewBox="0 0 566 323" preserveAspectRatio="none" aria-hidden="true">
      <defs>
        <linearGradient id="goldFill" x1="0" y1="0" x2="1" y2="1">
          <stop offset="0" stop-color="#a97f2c"/>
          <stop offset=".45" stop-color="#f3dc93"/>
          <stop offset="1" stop-color="#c49a3e"/>
        </linearGradient>
        <linearGradient id="blackFill" x1="0" y1="0" x2="1" y2="0">
          <stop offset="0" stop-color="#050505"/>
          <stop offset=".6" stop-color="#2a2a2a"/>
          <stop offset="1" stop-color="#0a0a0a"/>
        </linearGradient>
      </defs>
      <polygon class="band-top-black" points="0,0 566,0 566,52 355,52 385,80 0,80" fill="url(#blackFill)"/>
      <polygon class="band-top-gold" points="214,0 566,0 566,52 250,52" fill="url(#goldFill)"/>
      <polygon class="rule-top" points="0,80 385,80 390,85 0,85" fill="url(#goldFill)"/>
      <polygon class="rule-bottom" points="178,239 566,239 566,244 183,244" fill="url(#goldFill)"/>
      <polygon class="band-bottom-black" points="183,244 566,244 566,323 350,323 312,275 212,275" fill="url(#blackFill)"/>
      <polygon class="band-bottom-gold" points="0,275 312,275 350,323 0,323" fill="url(#goldFill)"/>
    </svg>

    <h1 class="holder-name">PETER LINDQVAR</h1>
    <p class="holder-title">DIRECTOR CRAFTSMAN</p>

    <div class="brand-back">
      <span class="brand-name">Marlowe</span>
      <span class="brand-sub">CABINETS</span>
    </div>

    <ul class="contact-list">
      <li class="contact-item">
        <span class="contact-icon">
          <svg width="26" height="18" viewBox="0 0 26 18" aria-hidden="true">
            <rect x="0" y="0" width="26" height="18" rx="2" fill="#07412a"/>
            <polyline points="1.5,2 13,10.5 24.5,2" fill="none" stroke="#d7b25c" stroke-width="2"/>
          </svg>
        </span>
        info@marlowecabinets.com.au
      </li>
      <li class="contact-item">
        <span class="contact-icon" aria-hidden="true"></span>
        @marlowe.cabinets
      </li>
    </ul>
  </section>
</main>
</body>
</html>
```